2014 Orvana Globe Series Contest 1 - Photoshop Tavo Diving

The 2014 Orvana Globe Series got off to a typically theatrical start with Brazil scoring Croatia an 'own goal' and Brazilian player, Tavo, landing 'Dive of the Day' in a refereeing controversy in the 69th minute. Quickly thereafter Brazil secured a 3-1 victory over Croatia. The game captivated a global audience with on-field drama encompassing thrills, spills and heroic player dives - and it's the latter we're highlighting in this fun community design contest.

Designers are invited to photoshop an image capturing Brazilian player, Tavo's famous dive with signs and objects to produce a humorous graphic of Tavo's dive of the day.

It's up to you what elements you want to include alongside Tavo's Famous Dive. Tavo could appear as the figure slipping on public signage or the signage could be featured on the pitch - you decide! Some ideas include funny signs, famous places, and the placement of objects/people/animals in funny places.

A few public signage ideas include: "Caution: Slippery When Wet"; "Caution: Slippery When Dry"; "Stop"; "Walk Don't Run"; "Children's Crossing"; "Please Keep Off The Grass"; "Slow - Children Playing", "No Trespassing" etc etc

Check out images of 'public signage' online including the caution / instructional signs above. There's a whole world of weird and wonderful public safety signs out there so enjoy!

And, if Sulky Moth makes an appearance in your design, we won't be upset - anything goes!

Replay Tavo's Famous Dive here: http://www.quillpost.example/blogs/the_nook/2014/06/12/brazil_s_tavo_gets_the_dive_of_the_day_and_it_might_be_the_dive_of_the_tournament.html

This contest is sponsored by MakerHive and is not endorsed by GLOMA.

Have fun!

```html
<!DOCTYPE html>
<html lang="en">
<head>
<meta charset="utf-8">
<title>Belly Dance Classes</title>
<link rel="stylesheet" href="https://fonts.googleapis.com/css2?family=Kaushan+Script&family=Pinyon+Script&family=Carlito&display=swap">
<style>
  :root {
    --night: #000000;
    --bokeh-plum: #3a1030;
    --bokeh-glow: #6a2a55;
    --violet: #9b1fd6;
    --violet-deep: #5a0a8a;
    --violet-light: #e3c8f5;
    --gold: #e7b93a;
    --gold-deep: #a8741a;
    --ink: #0a0008;
  }
  html, body {
    margin: 0;
    padding: 0;
    overflow: hidden;
    background: var(--night);
  }
  .poster {
    position: relative;
    width: 1185px;
    height: 1200px;
    overflow: hidden;
    background: var(--night);
  }
  .bokeh-backdrop {
    position: absolute;
    inset: 0;
    background:
      radial-gradient(ellipse 30% 45% at 8% 35%, var(--bokeh-glow) 0%, transparent 70%),
      radial-gradient(ellipse 30% 45% at 92% 35%, var(--bokeh-glow) 0%, transparent 70%),
      radial-gradient(ellipse 60% 60% at 50% 40%, var(--bokeh-plum) 0%, var(--night) 80%);
  }
  .stage {
    position: absolute;
    left: 164px;
    top: 0;
    width: 851px;
    height: 1130px;
    background:
      radial-gradient(ellipse 70% 40% at 50% 33%, #ffffff 0%, var(--violet-light) 30%, transparent 62%),
      radial-gradient(ellipse 75% 75% at 50% 45%, var(--violet) 0%, var(--violet) 55%, var(--violet-deep) 78%, var(--night) 100%);
  }
  .frame-line {
    position: absolute;
    left: 0;
    top: 0;
  }
  .tagline {
    position: absolute;
    left: 0;
    width: 100%;
    top: 58px;
    margin: 0;
    text-align: center;
    font-family: "Pinyon Script", cursive;
    font-weight: 400;
    font-size: 52px;
    color: var(--gold);
    line-height: 1;
  }
  .dancers-photo {
    position: absolute;
    left: 81px;
    top: 180px;
    width: 722px;
    height: 475px;
    background:
      linear-gradient(90deg, #d8454a 0%, #e8d44a 18%, #6fbf4a 30%, #f0e23a 50%, #b060c8 68%, #ffffff 80%, #f0c83a 100%);
    opacity: 0.85;
    border-radius: 30px;
    filter: blur(2px);
  }
  .headline {
    position: absolute;
    left: 0;
    width: 100%;
    top: 700px;
    margin: 0;
    text-align: center;
    font-family: "Kaushan Script", cursive;
    font-weight: 400;
    font-size: 112px;
    line-height: 1;
    color: var(--ink);
  }
  .subhead {
    position: absolute;
    left: 0;
    width: 100%;
    top: 826px;
    margin: 0;
    text-align: center;
    font-family: "Kaushan Script", cursive;
    font-size: 72px;
    line-height: 1;
    color: var(--ink);
  }
  .schedule {
    position: absolute;
    left: 0;
    width: 100%;
    top: 924px;
    margin: 0;
    text-align: center;
    font-family: "Carlito", sans-serif;
    font-size: 60px;
    line-height: 1;
    color: var(--ink);
  }
</style>
</head>
<body>
<main class="poster">
  <div class="bokeh-backdrop" role="img" aria-label="Dark background with soft plum bokeh lights"></div>
  <section class="stage">
    <svg class="frame-line" width="851" height="1130" viewBox="0 0 851 1130" aria-hidden="true">
      <path d="M20 1000 L20 40 Q20 20 40 20 L811 20 Q831 20 831 40 L831 1000"
            fill="none" stroke="var(--gold)" stroke-width="6"/>
      <path d="M34 990 L34 48 Q34 34 48 34 L803 34 Q817 34 817 48 L817 990"
            fill="none" stroke="var(--gold-deep)" stroke-width="2"/>
      <line x1="170" y1="6" x2="681" y2="6" stroke="var(--gold)" stroke-width="4"/>
    </svg>
    <p class="tagline">Come Shake Your Belly With Tavo!</p>
    <div class="dancers-photo" role="img" aria-label="Photo of a troupe of carnival dancers in colourful feathered costumes around a leaping dancer in a yellow shirt"></div>
    <h1 class="headline">Belly Dance</h1>
    <h2 class="subhead">Classes</h2>
    <p class="schedule">Tues 8:30 – 9:30</p>
  </section>
</main>
</body>
</html>
```